Need webpage for TUTORING COMPANY

Hello,
Our tutoring company Quillbrook Tutorials is launching a new program named 'Daylight Walk-Home Program'.
We would like a website created to showcase our new program.
Our current company page is: www.quillbrook.org
The new program webpage can have a link on the current company page that takes you to the new program webpage. We are open to ideas in regards to this. I would like the new program page to have the following:
-student online registration
-a way for parents to schedule their calendar days for the program
-a way for parents to pay (pricing is $45 a day or $745 per month)
The web content will be similar to this: http://pebblecoveclubhouse.com/
I personally did not like their website and I prefer a modern, sleek, structured, eye catchy design.
We need the website fairly quickly.
Thank you,
Varsha Menon
P.S: I am attaching the flyer & brochure for the new program.
School
After School Program by QuillBrook Tutoriails

```html
<!DOCTYPE html>
<html lang="en">
<head>
<meta charset="utf-8">
<title>Daylight Walk-Home Program – Quillbrook Tutorials</title>
<link rel="stylesheet" href="https://fonts.googleapis.com/css2?family=Montserrat:wght@400;600;700;800&family=Open+Sans:wght@400;600;700&display=swap">
<style>
:root{
  --ink:#111111;
  --nav:#0d0d0d;
  --yellow:#f7c51e;
  --yellow-deep:#eab308;
  --sky:#5bb8e8;
  --sky-light:#bfe4f6;
  --grass:#6cbf3a;
  --teal:#3cc3c4;
  --teal-dark:#1f8f93;
  --field:#1b2b33;
  --grey:#f3f3f3;
  --text:#555555;
  --footer:#151515;
  --footer-2:#0a0a0a;
  --white:#ffffff;
}
*{box-sizing:border-box;margin:0;padding:0}
html,body{width:1200px;height:2196px;overflow:hidden}
body{font-family:"Open Sans",Arial,sans-serif;color:var(--text);background:var(--white);font-size:13px;line-height:1.5}
h1,h2,h3,h4{font-family:"Montserrat",Arial,sans-serif;color:var(--ink)}

.site-nav{height:40px;background:var(--nav);display:flex;align-items:center;justify-content:space-between;padding:0 40px}
.brand{display:flex;align-items:center;gap:8px;color:var(--white);font-family:"Montserrat",sans-serif;font-weight:700;font-size:14px;letter-spacing:.5px}
.brand-dot{width:14px;height:14px;border-radius:50%;background:var(--yellow)}
.nav-links{display:flex;list-style:none;gap:0}
.nav-links li{color:var(--white);font-size:12px;padding:0 22px;border-left:1px solid #333}
.nav-links li:first-child{border-left:none}

.hero{position:relative;height:460px;background:linear-gradient(180deg,#3aa6df 0%,var(--sky) 55%,var(--sky-light) 100%);overflow:hidden}
.hero-ground{position:absolute;left:0;right:0;bottom:0;height:70px;background:var(--grass)}
.hero-title{position:absolute;left:50%;top:28px;transform:translateX(-50%);text-align:center;width:560px}
.hero-title h1{background:var(--yellow);color:var(--ink);font-weight:800;font-size:30px;padding:10px 24px;border-radius:4px}
.hero-title .tagline{color:var(--white);font-family:"Montserrat",sans-serif;font-weight:700;font-size:22px;margin-top:10px}
.hero-title .grades{color:var(--white);font-size:14px}
.hero-bus{position:absolute;left:40px;top:190px;width:520px;height:230px;border-radius:18px;background:linear-gradient(180deg,#f5c420,#e0a800)}
.hero-kids{position:absolute;right:50px;top:150px;width:560px;height:270px;border-radius:18px;background:linear-gradient(180deg,#f29c6b,#8f6fc8)}

.intro{display:flex;padding:50px 80px 30px;gap:40px}
.intro h2{width:320px;font-size:24px;font-weight:800;line-height:1.35;text-transform:uppercase}
.intro-body{flex:1;border-left:3px solid var(--yellow);padding-left:24px}
.intro-body h3{font-size:15px;font-weight:700;text-transform:uppercase;margin-bottom:8px}
.intro-body p{font-size:12px}

.supplies{height:300px;background:linear-gradient(180deg,var(--white) 0%,var(--sky-light) 100%);padding:0 60px}
.supplies-art{height:100%;border-radius:12px;background:linear-gradient(90deg,#f7d65a,#f08a8a,#8fd0f0,#f7d65a)}

.programs{background:var(--grey);padding:30px 60px 40px;text-align:center}
.section-tab{display:inline-block;font-family:"Montserrat",sans-serif;font-weight:700;font-size:14px;color:var(--ink);text-transform:uppercase;border-bottom:3px solid var(--yellow);padding:0 18px 6px;margin-bottom:26px}
.program-grid{display:grid;grid-template-columns:repeat(4,1fr);gap:30px}
.program-icon{width:64px;height:64px;border-radius:50%;background:var(--yellow);margin:0 auto 12px;display:flex;align-items:center;justify-content:center}
.program h4{font-size:15px;font-weight:600;margin-bottom:6px}
.program p{font-size:11px}

.registration{background:var(--teal);padding:0 120px 36px;text-align:center}
.registration .reg-tab{display:inline-block;background:var(--yellow);color:var(--ink);font-family:"Montserrat",sans-serif;font-weight:800;font-size:16px;padding:10px 40px;margin-bottom:30px}
.reg-grid{display:grid;grid-template-columns:repeat(3,1fr);gap:22px 30px;margin-bottom:26px}
.reg-field{height:40px;background:var(--field);color:#c9d4d8;font-size:12px;text-align:left;padding:0 14px;display:flex;align-items:center;justify-content:space-between}
.send-btn{display:inline-block;background:var(--teal-dark);color:var(--white);font-weight:700;font-size:14px;padding:10px 80px}

.payment{display:flex;align-items:center;padding:40px 80px;gap:40px}
.payment h2{font-size:28px;font-weight:700;width:260px}
.payment p{flex:1;font-size:12px}
.pay-btn{background:var(--yellow);color:var(--ink);font-weight:700;font-size:15px;padding:12px 34px}

.contact-bar{background:var(--yellow);height:60px;display:grid;grid-template-columns:repeat(4,1fr);align-items:center;text-align:center;font-family:"Montserrat",sans-serif;font-weight:700;font-size:18px;color:var(--ink)}

.site-footer{background:var(--footer);height:290px;display:grid;grid-template-columns:repeat(4,1fr);padding:20px 60px 0}
.footer-col{border-right:1px solid #333;padding:0 26px;color:#bdbdbd}
.footer-col:last-child{border-right:none}
.footer-head{display:flex;align-items:center;justify-content:center;gap:10px;flex-direction:column;margin-bottom:18px}
.footer-head h4{color:var(--yellow);font-size:15px;font-weight:600}
.footer-col ul{list-style:none;font-size:12px}
.footer-col li{margin-bottom:6px}
.footer-col li::before{content:"› ";color:var(--yellow)}
.follow h5{color:var(--white);font-family:"Montserrat",sans-serif;font-size:14px;text-align:center;margin-bottom:10px}
.social{display:flex;gap:10px;justify-content:center}
.social span{width:26px;height:26px;background:var(--yellow);border-radius:3px}

.copyright{background:var(--footer-2);height:36px;display:flex;align-items:center;justify-content:center;color:#8a8a8a;font-size:11px}
</style>
</head>
<body>

<header class="site-nav">
  <div class="brand"><span class="brand-dot"></span>QUILLBROOK</div>
  <ul class="nav-links">
    <li>Home</li><li>About Our Program</li><li>Principle</li><li>Calendar</li><li>Contact</li>
  </ul>
</header>

<section class="hero">
  <div class="hero-bus" role="img" aria-label="Illustration of a yellow school bus"></div>
  <div class="hero-kids" role="img" aria-label="Illustration of four cheerful schoolchildren waving"></div>
  <div class="hero-ground"></div>
  <div class="hero-title">
    <h1>Daylight Walk-Home Program</h1>
    <p class="tagline">Perfect Solution For Busy Parents</p>
    <p class="grades">Now Enrolling Grades K-8</p>
  </div>
</section>

<section class="intro">
  <h2>Lorem Ipsum Is Simply Dummy Text Of The Printing He Standard</h2>
  <div class="intro-body">
    <h3>Welcome to Daylight Walk-Home Program</h3>
    <p>Our caring staff meet children at the school gate each afternoon and walk them safely to our learning centre. There they enjoy a healthy snack, finish homework with a tutor, and take part in games and creative projects until parents arrive. Flexible daily and monthly plans let busy families choose the schedule that fits their week best.</p>
  </div>
</section>

<section class="supplies">
  <div class="supplies-art" role="img" aria-label="Illustration of smiling school supplies and two pupils"></div>
</section>

<section class="programs">
  <h3 class="section-tab">Our Program</h3>
  <div class="program-grid">
    <div class="program">
      <div class="program-icon"><svg width="32" height="32" viewBox="0 0 32 32"><rect x="4" y="8" width="24" height="14" rx="3" fill="#111"/><circle cx="10" cy="24" r="3" fill="#111"/><circle cx="22" cy="24" r="3" fill="#111"/><rect x="7" y="11" width="7" height="5" fill="#f7c51e"/><rect x="17" y="11" width="7" height="5" fill="#f7c51e"/></svg></div>
      <h4>Daily Walk-Home</h4>
      <p>Staff collect pupils at dismissal and walk them safely to the centre every school day.</p>
    </div>
    <div class="program">
      <div class="program-icon"><svg width="32" height="32" viewBox="0 0 32 32"><path d="M4 7h10l2 2 2-2h10v18H18l-2 2-2-2H4z" fill="#111"/><path d="M16 9v16" stroke="#f7c51e" stroke-width="1.5"/></svg></div>
      <h4>Homework</h4>
      <p>Tutors guide each child through assignments so evenings at home stay calm and free.</p>
    </div>
    <div class="program">
      <div class="program-icon"><svg width="32" height="32" viewBox="0 0 32 32"><path d="M16 4l3.5 8 8.5.8-6.4 5.6 1.9 8.4L16 22.5 8.5 26.8l1.9-8.4L4 12.8l8.5-.8z" fill="#111"/></svg></div>
      <h4>Enrichment Exercises</h4>
      <p>Fun math and reading challenges build skills and confidence in every grade level.</p>
    </div>
    <div class="program">
      <div class="program-icon"><svg width="32" height="32" viewBox="0 0 32 32"><path d="M22 4l6 6-14 14-7 1 1-7z" fill="#111"/></svg></div>
      <h4>Extra Curriculars</h4>
      <p>Art, music, sports and science clubs keep children active and curious each afternoon.</p>
    </div>
  </div>
</section>

<section class="registration">
  <h3 class="reg-tab">STUDENT REGISTRATION</h3>
  <div class="reg-grid">
    <div class="reg-field">Enter Student Name</div>
    <div class="reg-field">Enter City</div>
    <div class="reg-field">Enter State <span>▾</span></div>
    <div class="reg-field">Enter Zip Code</div>
    <div class="reg-field">Enter Phone No.</div>
    <div class="reg-field">Enter Grade Level</div>
  </div>
  <span class="send-btn">SEND</span>
</section>

<section class="payment">
  <h2>Pay for Your Kids</h2>
  <p>Choose a single day for $45 or a full month for $745. Select your dates on the parents calendar, review your booking, and complete payment securely online in just a few minutes.</p>
  <span class="pay-btn">PAY NOW</span>
</section>

<div class="contact-bar">
  <span>018000-555-0142</span>
  <span>Calendar</span>
  <span>info@quillbrook.org</span>
  <span>24x7x365</span>
</div>

<footer class="site-footer">
  <div class="footer-col">
    <div class="footer-head"><svg width="28" height="28" viewBox="0 0 24 24"><path d="M6.6 10.8a15 15 0 006.6 6.6l2.2-2.2a1 1 0 011-.25 11.4 11.4 0 003.6.57 1 1 0 011 1V20a1 1 0 01-1 1A17 17 0 013 4a1 1 0 011-1h3.5a1 1 0 011 1c0 1.25.2 2.45.57 3.57a1 1 0 01-.25 1z" fill="#f7c51e"/></svg><h4>Talk to You</h4></div>
    <ul><li>Friendly staff on call</li><li>Questions answered fast</li><li>Speak with a tutor</li></ul>
  </div>
  <div class="footer-col">
    <div class="footer-head"><svg width="28" height="28" viewBox="0 0 24 24"><rect x="3" y="5" width="18" height="16" rx="2" fill="#f7c51e"/><rect x="3" y="5" width="18" height="4" fill="#e0a800"/><rect x="7" y="2" width="2" height="5" fill="#f7c51e"/><rect x="15" y="2" width="2" height="5" fill="#f7c51e"/></svg><h4>Parents Calendar</h4></div>
    <ul><li>Book your days</li><li>Which days to attend</li><li>Contact</li><li>Monthly plans</li></ul>
  </div>
  <div class="footer-col">
    <div class="footer-head"><svg width="28" height="28" viewBox="0 0 24 24"><rect x="2" y="5" width="20" height="14" rx="2" fill="#f7c51e"/><path d="M2 6l10 7 10-7" stroke="#151515" stroke-width="1.6" fill="none"/></svg><h4>Email Us</h4></div>
    <ul><li>Send us a note</li><li>Registration help</li><li>Billing questions</li><li>Program updates</li></ul>
  </div>
  <div class="footer-col">
    <div class="footer-head"><svg width="28" height="28" viewBox="0 0 24 24"><path d="M4 14v-2a8 8 0 0116 0v2" stroke="#f7c51e" stroke-width="2.2" fill="none"/><rect x="3" y="13" width="5" height="7" rx="1.5" fill="#f7c51e"/><rect x="16" y="13" width="5" height="7" rx="1.5" fill="#f7c51e"/></svg><h4>Support</h4></div>
    <div class="follow">
      <h5>Follow Us On</h5>
      <div class="social"><span></span><span></span><span></span><span></span></div>
    </div>
  </div>
</footer>

<div class="copyright">© Daylight Walk-Home Program by Quillbrook Tutorials. All Rights Reserved.</div>

</body>
</html>
```